I will ask the design of the business card

We are looking for business card design of the new company "TORVIK QUANTA WORKS LLC." Based in Azerbaijan.
In case
We are working on Azerbaijan to set up the first exchange of crypto currencies.

The key currency used in exchanges is called "MELDA".
In case
We are doing project to make crypto currency infrastructure.

We provide state-of-the-art technology to the world.

```html
<!DOCTYPE html>
<html lang="en">
<head>
<meta charset="utf-8">
<title>Torvik Quanta Works LLC. — Business Card</title>
<link rel="stylesheet" href="https://fonts.googleapis.com/css2?family=Ubuntu:wght@400;500&display=swap">
<style>
  :root {
    --page: #f3f3f3;
    --ink: #0d0d0d;
    --paper: #ffffff;
    --orange: #e8521c;
    --gold-light: #efe1bf;
    --gold: #c9b07a;
    --gold-deep: #8f7442;
    --text-dark: #1c1c1c;
  }
  * { box-sizing: border-box; margin: 0; padding: 0; }
  html, body {
    width: 1133px; height: 1200px; overflow: hidden;
    background: var(--page);
    font-family: "Ubuntu", sans-serif;
  }
  .card {
    position: absolute;
    left: 174px;
    width: 785px; height: 453px;
    border-radius: 22px;
    overflow: hidden;
  }
  .card--front { top: 93px; background: var(--ink); }
  .card--back { top: 660px; background: var(--paper); }

  .artwork { position: absolute; }
  .card--front .artwork {
    left: 0; right: 0; top: 250px; bottom: 0;
    background: linear-gradient(168deg,
      var(--gold-deep) 0%, var(--gold) 22%, var(--gold-light) 38%,
      var(--orange) 52%, var(--paper) 68%, var(--paper) 100%);
    clip-path: polygon(0 20%, 100% 0, 100% 100%, 0 100%);
  }
  .card--back .artwork {
    top: 0; bottom: 0; left: 300px; right: 0;
    background: linear-gradient(125deg,
      var(--gold-light) 0%, var(--gold) 20%, var(--gold-deep) 34%, var(--ink) 52%, var(--ink) 100%);
    clip-path: polygon(15% 0, 100% 0, 100% 100%, 24% 100%);
  }

  .brand {
    position: absolute;
    color: var(--orange);
    font-weight: 400;
    text-transform: uppercase;
    line-height: 1.02;
    letter-spacing: 0.02em;
  }
  .card--front .brand { left: 314px; top: 108px; font-size: 38px; }
  .card--back .brand { left: 139px; top: 235px; font-size: 24px; }

  .website {
    position: absolute; right: 58px; bottom: 40px;
    font-size: 18px; letter-spacing: 0.08em;
    color: var(--text-dark);
  }

  .contact {
    position: absolute; left: 145px; top: 296px;
    list-style: none;
    font-size: 20px; line-height: 1.18; letter-spacing: 0.08em;
    color: var(--text-dark);
  }

  .social {
    position: absolute; right: 70px; bottom: 56px;
    display: flex; gap: 8px; list-style: none;
  }
  .social__item {
    width: 36px; height: 36px;
    background: var(--orange);
  }
</style>
</head>
<body>

<section class="card card--front" aria-label="Card front">
  <div class="artwork" role="img" aria-label="Abstract folded gold and orange ribbon artwork across the lower card"></div>
  <p class="brand">Torvik Quanta<br>Works LLC.</p>
  <p class="website">WEBSITE NAME</p>
</section>

<section class="card card--back" aria-label="Card back">
  <div class="artwork" role="img" aria-label="Abstract gold ribbon over a dark angled panel"></div>
  <p class="brand">Torvik Quanta<br>Works LLC.</p>
  <ul class="contact">
    <li>NAME</li>
    <li>ADDRESS</li>
    <li>EMAIL</li>
    <li>PHONE</li>
  </ul>
  <ul class="social" aria-label="Social links">
    <li class="social__item"></li>
    <li class="social__item"></li>
    <li class="social__item"></li>
  </ul>
</section>

</body>
</html>
```